Web Page Header (Header Only)

Our company would like to develop a new website header look for our business webpage theme. This header needs to look fantastic and add value to the overall professional appearance of our business and website design. We would like to incorporate into the design concept our company logo and use the slogan “Providing Effect Project Controls and Management Solutions” It would be great to promote our businesses global presence in the website header design concept.

For you to understand our business branding, images of our business cards, company brochure and Social Page page have been attached to this project. A PDF file of our company logo is also attached, our website address is www.brightlanepartners.com Please read the attached webpage header PDF document attached to this project as it will you assist with your design concept. Contained within the PDF is also an example of a webpage header design.

The graphic design work needs to done in Photoshop as our business utilizes CS6. The winning design concept will be integrated into our webpage theme using our original website developer. The graphics will need to fit the dimensions for our webpage header area for easy integration.
Updates

It would be great to promote our busineses global presence in the website header design concept

Project Deadline Extended
Reason: Some designers needed more time

Industry/Entity Type

Graphic Design

Requirements
Must have
• The webpage header design must be elegant, professional,reflect a market leader and be easily integrate into the webpage design.

```html
<!DOCTYPE html>
<html lang="en">
<head>
<meta charset="utf-8">
<title>Brightlane Partners</title>
<link href="https://fonts.googleapis.com/css2?family=Archivo+Black&family=Allerta+Stencil&family=Fjalla+One&family=Open+Sans:wght@400;600;700&display=swap" rel="stylesheet">
<style>
  :root {
    --frame: #6e6e6e;
    --page: #ffffff;
    --header-light: #f2f2f2;
    --header-mid: #c9c9c9;
    --brand-dark: #151515;
    --brand-red: #d3111d;
    --red-deep: #8d0711;
    --bar-dark: #2b2c2e;
    --bar-light: #5b5c5f;
    --text-grey: #8a8a8a;
    --card-border: #d6d6d6;
  }
  * { margin: 0; padding: 0; box-sizing: border-box; }
  html, body { width: 1200px; height: 1000px; overflow: hidden; }
  body { background: var(--frame); position: relative; font-family: "Open Sans", sans-serif; }

  .page { position: absolute; left: 1px; top: 55px; width: 1198px; height: 857px; background: var(--page); overflow: hidden; }

  .masthead { position: absolute; left: 0; top: 0; width: 1198px; height: 172px;
    background: linear-gradient(90deg, var(--header-light) 0%, #dcdcdc 45%, var(--header-mid) 70%, var(--header-light) 100%); }
  .brand { position: absolute; left: 26px; top: 44px; display: flex; align-items: center; gap: 16px; }
  .brand-mark { width: 48px; height: 48px; background: var(--brand-red); }
  .brand-name { font-family: "Archivo Black", sans-serif; font-size: 46px; color: var(--brand-dark); letter-spacing: -1px; line-height: 1; }
  .slogan { position: absolute; left: 167px; top: 112px; font-family: Arial, sans-serif; font-size: 15px; color: var(--brand-dark); }
  .values { position: absolute; left: 722px; top: 12px; width: 140px; text-align: center;
    font-family: "Allerta Stencil", sans-serif; font-size: 20px; line-height: 35px; color: #1d1d1d; letter-spacing: 1px; }
  .globe-photo { position: absolute; left: 958px; top: 8px; width: 212px; height: 164px; border-radius: 40px 40px 0 0;
    background: radial-gradient(circle at 60% 45%, #c9ccd0 0%, #e8c7a8 40%, #f1ece8 75%); }

  .sector-bar { position: absolute; left: 0; top: 170px; width: 1198px; height: 48px; border-radius: 0 22px 0 0;
    background: linear-gradient(180deg, #e0202b 0%, var(--brand-red) 45%, var(--red-deep) 100%);
    display: flex; align-items: center; padding-left: 43px; overflow: hidden;
    font-family: "Fjalla One", sans-serif; font-size: 18.5px; color: #fff; white-space: nowrap; }
  .sector-bar span.sep { margin: 0 11px; }

  .main-nav { position: absolute; left: 40px; top: 224px; width: 819px; height: 48px; border-radius: 4px;
    background: linear-gradient(180deg, var(--bar-light) 0%, var(--bar-dark) 60%, #1e1f20 100%);
    display: flex; align-items: center; padding-left: 29px; gap: 15px; }
  .main-nav a { color: #fff; text-decoration: none; font-size: 12.5px; text-transform: uppercase; }
  .main-nav a.current { color: #cfcfcf; }

  .welcome-head { position: absolute; left: 892px; top: 224px; width: 287px; height: 48px; border-radius: 4px;
    background: linear-gradient(180deg, var(--bar-light) 0%, var(--bar-dark) 60%, #1e1f20 100%);
    color: #fff; font-weight: 700; font-size: 17px; text-align: center; line-height: 44px; }
  .welcome-text { position: absolute; left: 897px; top: 282px; width: 278px; font-size: 12.6px; line-height: 23.4px;
    color: var(--text-grey); text-align: justify; }

  .slider { position: absolute; left: 40px; top: 322px; width: 820px; height: 336px;
    background: linear-gradient(90deg, #1a2127 0%, #2f3c45 30%, #1d4a66 55%, #0e2a3b 80%, #0a1820 100%); }
  .slider-arrow { position: absolute; top: 154px; width: 14px; height: 14px; background: rgba(120,120,120,.7); }
  .slider-arrow svg { display: block; }
  .slider-arrow.prev { left: 7px; } .slider-arrow.next { right: 6px; }
  .slider-caption { position: absolute; left: 275px; top: 228px; width: 545px; height: 76px; background: rgba(20,22,24,.72); padding: 5px 0 0 11px; color: #fff; }
  .slider-caption h2 { font-weight: 400; font-size: 29px; line-height: 38px; }
  .slider-caption p { font-size: 11.5px; margin-top: 4px; }

  .feature { position: absolute; top: 667px; width: 181px; height: 171px; }
  .feature-img { width: 100%; height: 100%; }
  .feature-bar { position: absolute; left: 0; bottom: 0; width: 100%; height: 28px; background: rgba(40,40,40,.85);
    display: flex; font-size: 12px; color: #fff; text-transform: uppercase; }
  .feature-bar .label { flex: 1; padding: 7px 0 0 5px; }
  .feature-bar .more { width: 83px; background: var(--brand-red); padding: 7px 0 0 3px; }

  .contact-card { position: absolute; left: 892px; width: 288px; height: 72px; border: 1px solid var(--card-border);
    background: linear-gradient(180deg, #ffffff 0%, #ececec 100%); }
  .contact-card .icon { position: absolute; left: 10px; top: 9px; width: 42px; height: 42px; border-radius: 3px;
    background: linear-gradient(180deg, #4a4a4a, #111); }
  .contact-card .icon svg { display: block; margin: 11px auto 0; }
  .contact-card h3 { position: absolute; left: 71px; top: 8px; font-size: 16px; font-weight: 700; color: var(--brand-red); }
  .contact-card p { position: absolute; left: 72px; top: 34px; font-size: 12px; color: #555; }
</style>
</head>
<body>
<div class="page">
  <header class="masthead">
    <div class="brand"><span class="brand-mark"></span><span class="brand-name">BRIGHTLANE PARTNERS</span></div>
    <div class="slogan">Providing Effective Project Controls and Management Solutions</div>
    <div class="values">KNOWLEDGE<br>EXPERATISE<br>EXPERIENCE<br>CAPACITY</div>
    <div class="globe-photo" role="img" aria-label="Hand holding a glass globe"></div>
  </header>

  <nav class="sector-bar">
    <span>Oil &amp; Gas</span><span class="sep">|</span><span>Minerals &amp; Metals</span><span class="sep">|</span><span>Petrochemical</span><span class="sep">|</span><span>Manufacturing</span><span class="sep">|</span><span>Building &amp; Construction</span><span class="sep">|</span><span>Telecommunication</span><span class="sep">|</span><span>Rail</span><span class="sep">|</span><span>Civil</span><span class="sep">|</span><span>New Industries</span>
  </nav>

  <nav class="main-nav">
    <a class="current" href="#">Home</a><a href="#">Services</a><a href="#">Benefits</a><a href="#">Management</a><a href="#">Planning</a><a href="#">Optimisation</a><a href="#">Industry</a><a href="#">Software</a><a href="#">Contact Us</a>
  </nav>

  <div class="welcome-head">WELCOME</div>
  <p class="welcome-text">Brightlane Partners provides effective project controls and management solutions to construction projects in Australia and Overseas. We provide services to both large multinational companies and smaller privately owned businesses. Our knowledge and expertise assist clients to effectively plan and manage their construction projects or project portfolios. Our focus is to provide your business with the tools, solutions and strategies necessary to deliver projects on time and within budget. We provide short or long term support, depending on your needs</p>

  <section class="slider" role="img" aria-label="Businessman with laptop beside glass office towers">
    <div class="slider-arrow prev"><svg width="14" height="14"><path d="M8 4 L5 7 L8 10" stroke="#fff" fill="none"/></svg></div>
    <div class="slider-arrow next"><svg width="14" height="14"><path d="M6 4 L9 7 L6 10" stroke="#fff" fill="none"/></svg></div>
    <div class="slider-caption"><h2>BRIGHTLANE PARTNERS</h2><p>KNOWLEDGE | EXPERTISE | EXPERIENCE | CAPACITY</p></div>
  </section>

  <article class="feature" style="left:40px">
    <div class="feature-img" role="img" aria-label="Business team standing before a world map" style="background:linear-gradient(180deg,#4a9be0 0%,#bcd9f2 45%,#6d6d6d 100%)"></div>
    <div class="feature-bar"><span class="label">Services</span><span class="more">Readmore»</span></div>
  </article>
  <article class="feature" style="left:250px">
    <div class="feature-img" role="img" aria-label="Coins, calculator and financial chart" style="background:linear-gradient(135deg,#f2eee6 0%,#c9b69a 45%,#7a7a7a 100%)"></div>
    <div class="feature-bar"><span class="label">Benefits of</span><span class="more">Readmore»</span></div>
  </article>
  <article class="feature" style="left:460px">
    <div class="feature-img" role="img" aria-label="Manager working at a desk" style="background:linear-gradient(180deg,#7b8fa6 0%,#4d6a8f 55%,#3a4350 100%)"></div>
    <div class="feature-bar"><span class="label">Management</span><span class="more">Readmore»</span></div>
  </article>
  <article class="feature" style="left:670px">
    <div class="feature-img" role="img" aria-label="Hand marking a project schedule chart" style="background:linear-gradient(135deg,#6a6a6a 0%,#e6e6e6 40%,#f7f3ee 100%)"></div>
    <div class="feature-bar"><span class="label">Planning</span><span class="more">Readmore»</span></div>
  </article>

  <aside class="contact-card" style="top:632px">
    <div class="icon"><svg width="24" height="18"><rect x="1" y="1" width="22" height="16" fill="none" stroke="#fff" stroke-width="1.5"/><path d="M1 1 L12 10 L23 1" fill="none" stroke="#fff" stroke-width="1.5"/></svg></div>
    <h3>Email Us</h3><p>Click here</p>
  </aside>
  <aside class="contact-card" style="top:715px">
    <div class="icon"></div>
    <h3>Social Page</h3><p>Follow us on</p>
  </aside>
  <aside class="contact-card" style="top:798px">
    <div class="icon"></div>
    <h3>Network Page</h3><p>Follow us on</p>
  </aside>
</div>
</body>
</html>
```